Brisk Lantern Estates, which offers a selection of prime properties (villas

A website that contains: Idea, benefits, destinations (villas), offers, about us, contact, newsletter, social media, blog, look at the attachment, even if it is in German. The idea is that I can easily add new pages, if necessary, with the design you make. Later on we want to add a reservation system, so you can book your villa through the internet. Besides, there is a concierge service available, which organizes everything for the customer, owner, from villa to restaurant, limo service, ... & benefits and emotions through nice pictures / videos, they should be convinced to invest.

Target Market(s)

Investors (golfer and non-golfer) which have 300'000 to invest in a kind of real-estate investing club

Number of Pages Required

5+ page

Font styles to use
Sans Serif

Requirements
Must have
• It must be for wordpress, must have an exclusive touch, high quality, with nice pictures of golf courses. The Logo is gold so it has to match with gold, the font is segan or segoe semilight or similar, sans serif
Nice to have
• may be as well as the possibility to include videos of the different destinations and houses

```html
<!DOCTYPE html>
<html lang="en">
<head>
<meta charset="utf-8">
<title>Brisk Lantern Estates</title>
<link href="https://fonts.googleapis.com/css2?family=Open+Sans:wght@300;400;600;700&display=swap" rel="stylesheet">
<style>
:root{
  --gold:#d9a92c;
  --gold-soft:#e6bf5a;
  --ink:#1e1e1e;
  --panel:#232323;
  --text:#555;
  --light:#f4f4f4;
  --white:#fff;
}
*{box-sizing:border-box;margin:0;padding:0}
html,body{width:1200px;height:1200px;overflow:hidden;background:var(--white);font-family:"Open Sans",sans-serif;color:var(--text)}
.page{width:1200px;height:1200px;overflow:hidden;position:relative}

/* hero */
.hero{position:relative;height:560px;color:var(--white);
  background:linear-gradient(180deg,#151208 0%,#2a2010 30%,#5a4218 55%,#3a2c12 75%,#1b150b 100%)}
.hero-photo{position:absolute;inset:0;
  background:radial-gradient(ellipse at 70% 45%,rgba(230,170,70,.45),transparent 55%),radial-gradient(ellipse at 25% 70%,rgba(200,140,50,.3),transparent 50%)}
.topbar{position:absolute;top:0;right:70px;display:flex;align-items:center;gap:14px;height:36px}
.phone{background:var(--gold);color:var(--white);font-size:13px;padding:0 16px;height:36px;display:flex;align-items:center;gap:8px}
.social{display:flex;gap:10px}
.social span{width:22px;height:22px;border:1.5px solid #ddd;border-radius:50%}
.pill{border:1px solid #ddd;border-radius:12px;font-size:11px;padding:3px 12px;color:#eee}
.brand{position:absolute;left:80px;top:70px;display:flex;align-items:center;gap:10px}
.brand-dot{width:22px;height:22px;border:2px solid var(--gold)}
.brand-name{color:var(--gold);font-size:15px;font-weight:400;letter-spacing:.5px}
.nav{position:absolute;right:70px;top:78px;display:flex;gap:30px;font-size:12px;letter-spacing:.4px}
.nav a{color:#eee;text-decoration:none}
.nav a.active{border-bottom:2px solid #fff;padding-bottom:4px}
.hero-copy{position:absolute;left:80px;top:220px;width:640px}
.hero-copy h1{font-weight:300;font-size:60px;line-height:1.2}
.hero-copy p{font-size:17px;line-height:1.7;margin-top:26px;font-weight:400}

/* press */
.press{height:110px;background:var(--light);display:flex;align-items:center;justify-content:space-around;padding:0 60px}
.press-item{display:flex;align-items:center;gap:8px;color:#666;font-size:20px;font-weight:600}
.press-item i{width:14px;height:14px;border-radius:50%;background:#888;display:block}

/* who we are */
.about{display:flex;padding:48px 80px 40px;gap:60px;height:340px}
.about-text{width:460px}
.about h2{font-weight:400;font-size:30px;color:var(--ink);margin-bottom:22px}
.about p{font-size:13.5px;line-height:1.7;margin-bottom:14px}
.btn{display:inline-block;background:var(--gold);color:var(--white);font-size:12px;font-weight:600;padding:8px 22px;margin-top:8px}
.about-photo{flex:1;height:250px;background:linear-gradient(135deg,#d9d9d9,#8a8a8a 60%,#4a4a4a)}

/* services */
.services{display:flex;height:350px}
.services-photo{width:600px;background:linear-gradient(180deg,#6f9ed0 0%,#3f7a3a 45%,#2d5a2a 65%,#2aa6d6 80%,#1976b8 100%)}
.services-list{flex:1;background:var(--panel);color:#ddd;padding:36px 60px}
.services-list h2{font-weight:400;font-size:30px;color:var(--white);margin-bottom:24px}
.service{display:flex;align-items:center;gap:18px;margin-bottom:16px;font-size:13px;line-height:1.5}
.service-icon{width:46px;height:46px;flex:none;border:1.5px solid var(--gold);border-radius:50%;display:flex;align-items:center;justify-content:center}
</style>
</head>
<body>
<div class="page">
  <header class="hero">
    <div class="hero-photo" role="img" aria-label="Night view of a river city with a lit chain bridge"></div>
    <div class="topbar">
      <div class="phone">
        <svg width="14" height="14" viewBox="0 0 24 24"><path d="M6 2l4 4-2 3c1 3 4 6 7 7l3-2 4 4-3 4C10 22 2 14 2 5z" fill="#fff"/></svg>
        +41 44 000 12 34
      </div>
      <div class="social"><span></span><span></span><span></span><span></span><span></span></div>
      <span class="pill">Sign In</span>
      <span class="pill">New user? Sign Up</span>
    </div>
    <div class="brand"><span class="brand-dot"></span><span class="brand-name">BRISK LANTERN ESTATES</span></div>
    <nav class="nav">
      <a class="active">HOME</a><a>IDEA</a><a>BENEFITS</a><a>DESTINATIONS (VILLAS)</a><a>OFFERS</a><a>ABOUT US</a><a>CONTACT</a><a>BLOG</a>
    </nav>
    <div class="hero-copy">
      <h1>A Selection Of<br>Prestige Golf Homes<br>To invest and enjoy</h1>
      <p>BRISK LANTERN ESTATES connects you with very experienced people, who invest in, own and build commercial real estate.</p>
    </div>
  </header>

  <section class="press">
    <div class="press-item">Northbay Finance</div>
    <div class="press-item"><i></i>CORVEL WIRE</div>
    <div class="press-item">Harbor Ledger</div>
    <div class="press-item">Tradeline</div>
    <div class="press-item">Meridian TV</div>
  </section>

  <section class="about">
    <div class="about-text">
      <h2>Who We Are</h2>
      <p>Brisk Lantern Estates offers the intermediation service for purchase, sale, lease, reform and maintenance of real estate; creates spaces contemplating their use according to the needs of the clients.</p>
      <p>Offering, thus, owners, investors and allies, tranquility and profitability, working with reliable and trained personnel through a management by processes aimed at surpassing the expectations of attention and service.</p>
      <span class="btn">READ MORE</span>
    </div>
    <div class="about-photo" role="img" aria-label="Business team meeting around a table"></div>
  </section>

  <section class="services">
    <div class="services-photo" role="img" aria-label="Resort pool surrounded by palm trees and loungers"></div>
    <div class="services-list">
      <h2>Our Services</h2>
      <div class="service"><span class="service-icon"><svg width="22" height="22" viewBox="0 0 24 24" fill="none" stroke="#fff" stroke-width="1.6"><path d="M3 11l9-7 9 7M6 9v11h12V9"/></svg></span>Property search, sale and Construction</div>
      <div class="service"><span class="service-icon"><svg width="22" height="22" viewBox="0 0 24 24"><text x="12" y="18" text-anchor="middle" font-size="18" font-family="Open Sans,sans-serif" font-weight="700" fill="#fff">$</text></svg></span>Providing assistance in securing funding for your investment property or your first home</div>
      <div class="service"><span class="service-icon"><svg width="22" height="22" viewBox="0 0 24 24" fill="none" stroke="#fff" stroke-width="1.6"><path d="M4 11l8-7 8 7v9H4z"/><rect x="9" y="12" width="6" height="5"/></svg></span>Smart Investor Premium service to our property investors for exclusive deals and investment property research</div>
      <div class="service"><span class="service-icon"><svg width="22" height="22" viewBox="0 0 24 24" fill="none" stroke="#fff" stroke-width="1.6"><circle cx="12" cy="9" r="5"/><path d="M9 13l-2 8 5-3 5 3-2-8"/></svg></span>Smart Partner Partnership program for our seasoned property investors</div>
    </div>
  </section>
</div>
</body>
</html>
```